Loftvane.ca Your Canadian Source for all your mortgage needs.

I need to get a fresh look on my current website. It is not currently a Wordpress site and i need to build a whole new site that i can do my editing in using Wordpress.
I need it built in a mobile or responsive theme.
There will be a secured application page which is critical.
I have 3 books written so i want to be able to have advertising spaces for promoting them and a landing page ( I can build my own landing pages)
I need the frame work of a professional theme with easy editing capabilities.
I have my own LOGOs which i would continue to use. The current site can be reviewed at www.loftvane.ca.
The front page could have a young couple near a nice house, open to suggestions.
I don't need a blog post to update but if it was on the sides of the pages I could use it. Something like a "Latest News" section.
I would like to have a Main page, Application Page, Resource page, Contact page, Calculator Page, a questions and answer page. Theses can be populated with the current information or I can add latter.
I want the main page to be a mini sales page so I can link to Posts on First Time Home Buyers, Refinance Options, Second Home or New purchase options.
I provide mortgages for people across Canada so i want the Canadian Flag incorporated
I like the colors to work with the logo colors on the current site

Target Market(s)

Canadian Mortgage Clients

Font styles to use
Sans Serif

Colors
3277b5
cadf82

Requirements
Must have
• Must work in a Wordpress Theme
• Please see Project description for more details
Nice to have
• Space to add banner ads for my books. I have 3 books written

```html
<!DOCTYPE html>
<html lang="en">
<head>
<meta charset="utf-8">
<title>Loftvane.ca – Your Canadian Source for Mortgages</title>
<link href="https://fonts.googleapis.com/css2?family=PT+Sans:wght@400;700&display=swap" rel="stylesheet">
<style>
:root{
  --blue:#3277b5;
  --blue-dark:#1f5d94;
  --green:#cadf82;
  --ink:#333b44;
  --muted:#7a8089;
  --page:#f1f1ef;
  --card:#ffffff;
  --line:#dcdcdc;
  --footer:#3a3d42;
  --footer-text:#a9adb3;
}
*{box-sizing:border-box;margin:0;padding:0}
html,body{width:809px;height:1200px;overflow:hidden}
body{font-family:"PT Sans",Arial,sans-serif;color:var(--ink);background:var(--page)}
.site{position:relative;width:809px;height:1200px;overflow:hidden;
  background:linear-gradient(180deg,#fbf6f4 0%,var(--page) 60%)}

/* header */
.site-header{position:absolute;top:0;left:0;width:809px;height:28px;background:#fff;border-bottom:1px solid var(--line)}
.brand{position:absolute;left:68px;top:5px;display:flex;align-items:center;gap:5px}
.brand-mark{width:14px;height:14px;background:var(--green)}
.brand-name{font-weight:700;font-size:15px;color:var(--blue);letter-spacing:.5px;line-height:1}
.main-nav{position:absolute;right:68px;top:0;display:flex;height:28px}
.main-nav a{font-size:8.5px;color:var(--muted);text-decoration:none;padding:0 10px;line-height:28px}
.main-nav a.is-active{color:var(--blue);border-bottom:2px solid var(--blue)}

/* hero */
.hero{position:absolute;top:28px;left:0;width:809px;height:364px;
  background:linear-gradient(160deg,#c9d6e2 0%,#a7b3a3 45%,#8a7d6f 70%,#6f7b57 100%)}
.hero-box{position:absolute;left:68px;top:210px;width:229px;height:140px;background:rgba(50,119,181,.92);padding:14px 14px}
.hero-box h1{color:#fff;font-size:21px;font-weight:700;margin-bottom:6px}
.hero-box p{color:#dfe9f3;font-size:8px;line-height:1.35;margin-bottom:10px}
.btn-dark{display:inline-block;background:#1b2430;color:#fff;font-size:8px;padding:6px 10px}
.hero-dots{position:absolute;left:460px;top:330px;display:flex;gap:5px}
.hero-dots span{width:5px;height:5px;border-radius:50%;background:rgba(255,255,255,.6)}
.hero-dots span.on{background:#fff}

/* welcome */
.welcome{position:absolute;left:68px;top:410px;width:392px}
.welcome h2{font-size:20px;font-weight:400;color:var(--blue);margin-bottom:12px}
.welcome p{font-size:8px;line-height:1.55;color:var(--muted);margin-bottom:9px}
.btn{display:inline-block;background:var(--blue);color:#fff;font-size:7.5px;padding:6px 11px;margin-top:4px}

/* promo cards */
.promo{position:absolute;left:475px;width:249px;background:var(--card);border:1px solid var(--line);padding:12px 12px}
.promo h3{font-size:17px;font-weight:700;color:var(--blue);margin-bottom:5px}
.promo p{font-size:7px;color:var(--muted);line-height:1.4;width:120px;margin-bottom:10px}
.promo .book{position:absolute;right:12px;top:14px;width:64px;height:92px}
.promo-buyers{top:408px;height:128px}
.promo-credit{top:552px;height:130px}
.promo-mortgage{top:698px;height:148px}

/* tiles */
.tile{position:absolute;top:708px;height:135px;width:189px;padding:12px}
.tile-apply{left:68px;background:linear-gradient(135deg,#2b2f36,#4c5563)}
.tile-calc{left:265px;background:linear-gradient(135deg,#5d8fb8,#c9d3dc)}
.tile span{position:absolute;left:12px;bottom:14px;color:#fff;font-size:8px;line-height:1.1}
.tile span b{display:block;font-size:17px;font-weight:400}

/* blog */
.blog-title{position:absolute;left:68px;top:872px;font-size:20px;font-weight:700;color:var(--blue)}
.blog-nav{position:absolute;right:68px;top:878px;display:flex;gap:8px}
.post{position:absolute;top:926px;height:190px}
.post .thumb{height:141px;width:100%}
.post h4{font-size:11px;font-weight:400;color:var(--blue);margin-top:12px}
.post time{display:block;font-size:6.5px;color:var(--muted);margin-top:3px}
.post-1{left:68px;width:216px}
.post-2{left:297px;width:216px}
.post-3{left:521px;width:208px}

/* footer */
.site-footer{position:absolute;left:0;top:1130px;width:809px;height:70px;background:var(--footer);padding:12px 68px}
.footer-links{font-size:7px;color:var(--footer-text)}
.footer-copy{font-size:6.5px;color:#80858c;margin-top:5px}
.social{position:absolute;right:68px;top:12px;display:flex;gap:8px}
.social span{width:10px;height:10px;border-radius:50%;background:var(--footer-text)}
</style>
</head>
<body>
<div class="site">

  <header class="site-header">
    <div class="brand"><span class="brand-mark"></span><span class="brand-name">LOFTVANE</span></div>
    <nav class="main-nav">
      <a href="#" class="is-active">Home</a>
      <a href="#">Application</a>
      <a href="#">Resource</a>
      <a href="#">Calculator</a>
      <a href="#">Q&amp;A</a>
      <a href="#">Contact</a>
    </nav>
  </header>

  <section class="hero" role="img" aria-label="Smiling young couple in front of a brick family house">
    <div class="hero-box">
      <h1>We get you started</h1>
      <p>Professional mortgage solutions for you and your family, helping you reach the home you have been dreaming of.</p>
      <span class="btn-dark">Get Started</span>
    </div>
    <div class="hero-dots"><span class="on"></span><span></span><span></span></div>
  </section>

  <section class="welcome">
    <h2>Welcome to Loftvane</h2>
    <p>At Loftvane.ca we make it simple for you and your family to find a mortgage that fits your budget. Whether it is your first home or your next move, our team is here to guide you every step.</p>
    <p>Our mortgage specialists work with lenders across Canada to secure competitive rates and flexible terms, so you can focus on the home you love.</p>
    <p>Start your application online today and get a quick answer.</p>
    <p>We believe that every Canadian deserves clear advice. Browse our resources, use the calculator, and read our guides to plan your purchase with confidence.</p>
    <span class="btn">Read More</span>
  </section>

  <article class="promo promo-buyers">
    <h3>Home Buyers</h3>
    <p>We will help you find the perfect rate for you.</p>
    <span class="btn">View Article</span>
    <div class="book" role="img" aria-label="Book cover for home buyers guide" style="background:linear-gradient(160deg,#c23a2b,#e9b04c)"></div>
  </article>
  <article class="promo promo-credit">
    <h3>Fix Credit</h3>
    <p>We will help you rebuild your credit step by step.</p>
    <span class="btn">View Article</span>
    <div class="book" role="img" aria-label="Book cover for credit repair guide" style="background:linear-gradient(160deg,#2b2b2b,#7f8a3a)"></div>
  </article>
  <article class="promo promo-mortgage">
    <h3>Mortgage</h3>
    <p>We will help you choose the right mortgage for you.</p>
    <span class="btn">View Article</span>
    <div class="book" role="img" aria-label="Book cover for mortgage guide" style="background:linear-gradient(160deg,#6fa04a,#e6e1b5)"></div>
  </article>

  <a class="tile tile-apply" href="#" role="img" aria-label="Hands typing on a laptop"><span>Mortgage<b>Apply Online</b></span></a>
  <a class="tile tile-calc" href="#" role="img" aria-label="Calculator and paperwork on a desk"><span>Mortgage<b>Calculator</b></span></a>

  <h2 class="blog-title">Recent Blog</h2>
  <div class="blog-nav">
    <svg width="10" height="12" viewBox="0 0 10 12"><path d="M7 1 2 6l5 5" fill="none" stroke="#333b44" stroke-width="2"/></svg>
    <svg width="10" height="12" viewBox="0 0 10 12"><path d="M3 1l5 5-5 5" fill="none" stroke="#333b44" stroke-width="2"/></svg>
  </div>

  <article class="post post-1">
    <div class="thumb" role="img" aria-label="Young couple holding house keys" style="background:linear-gradient(135deg,#8fa9bf,#d8c7b0)"></div>
    <h4>First Time Home Buyers</h4><time>July 28, 2015</time>
  </article>
  <article class="post post-2">
    <div class="thumb" role="img" aria-label="Couple reviewing refinance papers at home" style="background:linear-gradient(135deg,#c9b8a3,#7e8a99)"></div>
    <h4>Refinance Options</h4><time>July 28, 2015</time>
  </article>
  <article class="post post-3">
    <div class="thumb" role="img" aria-label="Couple meeting with a mortgage advisor" style="background:linear-gradient(135deg,#e6e6e6,#8d9aa8)"></div>
    <h4>Second Home or New purchase...</h4><time>July 28, 2015</time>
  </article>

  <footer class="site-footer">
    <div class="footer-links">Home | Our Team | Forms | Q &amp; A | Privacy | Contact</div>
    <div class="footer-copy">© 2015 Loftvane.ca. All rights reserved.</div>
    <div class="social"><span></span><span></span><span></span><span></span></div>
  </footer>

</div>
</body>
</html>
```